Business card design for Plumbing and Gas fitting company

We need a business card design for our plumbing and gas fitting company using the company logo and director details. Design should be modern and eye-catching however kept reasonably simple. This design should be targeted at commercial businesses/work so professionalism is key.

Target Market(s)

Commercial/business

Industry/Entity Type

Plumbing

Contact Information for Business Card

Warren Dohey
Director
027 581 9043
warren@vantorplumbingandgas.example
PO Box 7816
Palmerston North 4472

Font styles to use
Sans Serif

Requirements
Must have
• Logo
• Modern
• Kept simple
Nice to have
• Colour scheme based around logo

```html
<!DOCTYPE html>
<html lang="en">
<head>
<meta charset="utf-8">
<title>Vantor Plumbing &amp; Gas – Business Card</title>
<link rel="stylesheet" href="https://fonts.googleapis.com/css2?family=Poppins:wght@400;500;600&display=swap">
<style>
  :root {
    --backdrop: #0c3459;
    --card-white: #ffffff;
    --brand-blue: #0a78c2;
    --brand-orange: #e5823a;
    --text-white: #ffffff;
  }
  * { box-sizing: border-box; margin: 0; padding: 0; }
  html, body {
    width: 1200px; height: 900px; overflow: hidden;
    background: var(--backdrop);
    font-family: "Poppins", sans-serif;
  }
  .canvas { position: relative; width: 1200px; height: 900px; }

  .card {
    position: absolute;
    width: 600px; height: 343px;
    border-radius: 26px;
    overflow: hidden;
    background: var(--card-white);
    box-shadow: 0 14px 30px rgba(0, 0, 0, 0.35);
  }

  /* Front */
  .card--front { left: 80px; top: 70px; }
  .front__brand {
    position: absolute; left: 0; right: 0; top: 120px;
    display: flex; align-items: center; justify-content: center; gap: 14px;
  }
  .brand-dot {
    width: 26px; height: 26px; border-radius: 50%;
    background: var(--brand-orange);
  }
  .brand-name {
    font-weight: 600; font-size: 30px; color: var(--brand-blue);
    letter-spacing: 0.2px;
  }
  .front__band {
    position: absolute; left: 0; right: 0; bottom: 0; height: 58px;
    background: var(--brand-blue);
    display: flex; align-items: center; justify-content: center;
  }
  .website {
    color: var(--text-white); font-size: 13px; letter-spacing: 3px;
  }

  /* Back */
  .card--back { left: 520px; top: 487px; }
  .back__shapes { position: absolute; inset: 0; }
  .back__brand {
    position: absolute; left: 34px; top: 60px;
    display: flex; align-items: center; gap: 9px;
  }
  .back__brand .brand-name { font-size: 18px; }
  .back__brand .brand-dot { width: 16px; height: 16px; }
  .address {
    position: absolute; left: 34px; bottom: 12px;
    color: var(--text-white); font-size: 11.5px; line-height: 1.55; letter-spacing: 1px;
  }
  .contact {
    position: absolute; right: 30px; top: 104px;
    text-align: right; color: var(--text-white);
  }
  .contact__name { font-weight: 600; font-size: 24px; letter-spacing: 1px; line-height: 1.1; }
  .contact__role { font-size: 12px; letter-spacing: 1px; margin-bottom: 18px; }
  .contact__list { list-style: none; font-size: 11px; letter-spacing: 0.8px; line-height: 1.75; }
  .contact__list li { display: flex; align-items: center; justify-content: flex-end; gap: 8px; }
  .icon { width: 11px; height: 11px; fill: var(--text-white); flex: none; }
</style>
</head>
<body>
<main class="canvas">

  <section class="card card--front" aria-label="Card front">
    <div class="front__brand">
      <span class="brand-name">Vantor Plumbing &amp; Gas</span>
      <span class="brand-dot"></span>
    </div>
    <div class="front__band">
      <span class="website">www.vantorplumbingandgas.example</span>
    </div>
  </section>

  <section class="card card--back" aria-label="Card back">
    <svg class="back__shapes" viewBox="0 0 600 343" width="600" height="343" aria-hidden="true">
      <path d="M288 0 H600 V343 H0 V270 H70 C190 228 282 130 288 0 Z" fill="var(--brand-orange)"/>
      <path d="M336 0 H600 V343 H0 V292 H115 C235 252 328 150 336 0 Z" fill="var(--brand-blue)"/>
    </svg>

    <div class="back__brand">
      <span class="brand-name">Vantor Plumbing &amp; Gas</span>
      <span class="brand-dot"></span>
    </div>

    <p class="address">PO Box 7816<br>Palmerston North 4472</p>

    <div class="contact">
      <h1 class="contact__name">Warren Dohey</h1>
      <p class="contact__role">Director</p>
      <ul class="contact__list">
        <li>027 581 9043
          <svg class="icon" viewBox="0 0 24 24"><path d="M6.6 10.8a15 15 0 0 0 6.6 6.6l2.2-2.2a1 1 0 0 1 1-.25 11.4 11.4 0 0 0 3.6.57 1 1 0 0 1 1 1V20a1 1 0 0 1-1 1A17 17 0 0 1 3 4a1 1 0 0 1 1-1h3.5a1 1 0 0 1 1 1c0 1.25.2 2.45.57 3.57a1 1 0 0 1-.25 1z"/></svg>
        </li>
        <li>000 000-0000
          <svg class="icon" viewBox="0 0 24 24"><path d="M6 2h12v6H6zM3 9h18a1 1 0 0 1 1 1v8h-4v4H6v-4H2v-8a1 1 0 0 1 1-1zm5 8v3h8v-3z"/></svg>
        </li>
        <li>warren@vantorplumbingandgas.example
          <svg class="icon" viewBox="0 0 24 24"><path d="M2 4h20v16H2zm2 2v.5l8 5 8-5V6zm0 3v9h16V9l-8 5z"/></svg>
        </li>
        <li>www.vantorplumbingandgas.example
          <svg class="icon" viewBox="0 0 24 24"><path d="M12 2a10 10 0 1 0 0 20 10 10 0 0 0 0-20zm-1 17.9A8 8 0 0 1 4.1 11H7c.1 3.2 1.5 6.4 4 8.9zM4.1 13zM13 19.9c2.5-2.5 3.9-5.7 4-8.9h2.9A8 8 0 0 1 13 19.9zM9 11h6c-.1 2.6-1.2 5.1-3 7-1.8-1.9-2.9-4.4-3-7zm0-2c.1-2.6 1.2-5.1 3-7 1.8 1.9 2.9 4.4 3 7zm8 0c-.1-3.2-1.5-6.4-4-8.9A8 8 0 0 1 19.9 9zM7 9H4.1A8 8 0 0 1 11 2.1C8.5 4.6 7.1 7.8 7 9z"/></svg>
        </li>
      </ul>
    </div>
  </section>

</main>
</body>
</html>
```